Business Cards for Bramblewood Coatings Pty Ltd

Hi every one i need a design for my buisness cards. I Want my logo in it and the name of the company needs to stand out Bramblewood Coatings Pty Ltd. I want the background of the buisness cards black and i want the font to stand out in either a white or a silver stylish text. I want the design to be simple but original not to in your face if you know what i mean. I want on the back of the buisness cards to have the services that my buisness offers.
• Interior/Exterior
• Residential/Commercial
• Special effects/Texture Coatings
• Water Damage Repair
• Fully qualified
• Pensioner Discount
• 10 Year guarantee
• Fully Insured
• Obligation free quotes
full internal repaints include a proffesionla cleaning service
I want the services on the back to be layed out in an originall way not just dot points. If possible could my logo take up the whole back ground of the back but the text with the services be kind of like transparent so u cvan still see the logo i dont know if its possible it woiuld just look cool if possible. When i pick a design ill give my contact details to the designer to add to the design at the end. Any questions please just ask! Ill upload my logo.
Conatcs will include office phone: Mobile: E-mail - dean@bramblewoodcoatings.com.au, Ill also have a Postal address which is a PO Box and my website is www.bramblewoodcoatings.com.au

```html
<!DOCTYPE html>
<html lang="en">
<head>
<meta charset="utf-8">
<title>Bramblewood Coatings Pty Ltd – Business Cards</title>
<link href="https://fonts.googleapis.com/css2?family=Arimo:wght@400;700&display=swap" rel="stylesheet">
<style>
  :root {
    --bg: #d9d6d1;
    --card: #0b0b0b;
    --green: #9ccc3c;
    --green-dark: #6e9e1e;
    --white: #ffffff;
    --ink: #111111;
  }
  * { margin: 0; padding: 0; box-sizing: border-box; }
  html, body { width: 1200px; height: 900px; overflow: hidden; }
  body {
    background: var(--bg);
    font-family: "Arimo", Arial, sans-serif;
    position: relative;
  }
  .card {
    position: absolute;
    top: 283px;
    width: 496px;
    height: 303px;
    background: var(--card);
    border-radius: 14px;
    overflow: hidden;
    color: var(--white);
  }
  .card--front { left: 100px; }
  .card--back { left: 632px; }

  .brand-square {
    position: absolute;
    background: var(--green);
    border-radius: 3px;
    box-shadow: 4px 4px 0 var(--green-dark);
  }
  .brand-name {
    position: absolute;
    font-weight: 700;
    color: var(--white);
    text-transform: uppercase;
    line-height: 1.2;
  }

  /* front */
  .card--front .brand-square { left: 76px; top: 53px; width: 88px; height: 92px; }
  .card--front .brand-name { left: 196px; top: 84px; font-size: 21px; }

  .contact-band {
    position: absolute;
    left: 0; top: 197px;
    width: 484px; height: 92px;
    background: var(--green);
    border-radius: 0 14px 14px 0;
    color: var(--ink);
    font-size: 13px;
  }
  .contact-band .address {
    position: absolute; left: 34px; top: 14px;
    line-height: 23px;
  }
  .contact-band .address strong { font-weight: 700; }
  .contact-band .lines {
    position: absolute; left: 244px; top: 14px;
    list-style: none; line-height: 23px;
  }
  .contact-band .lines li { display: flex; align-items: center; gap: 8px; }
  .contact-band .lines svg { width: 12px; height: 12px; flex: none; }

  /* back */
  .holder { position: absolute; left: 36px; top: 92px; }
  .holder-name { color: var(--green); font-weight: 700; font-size: 20px; }
  .holder-role { font-size: 15px; margin-top: 2px; }

  .card--back .brand-square { left: 328px; top: 47px; width: 70px; height: 72px; }
  .card--back .brand-name {
    left: 246px; top: 130px; width: 240px;
    text-align: center; font-size: 17px;
  }

  .services {
    position: absolute; left: 13px; top: 202px;
    width: 466px; height: 64px;
    background: var(--green);
    border-radius: 10px;
    color: var(--ink);
    font-size: 11px;
    text-align: center;
    display: flex; flex-direction: column; justify-content: center;
    line-height: 19px;
  }
  .website {
    position: absolute; left: 13px; top: 276px; width: 466px;
    text-align: center; font-size: 11px; letter-spacing: 0.3px;
  }
</style>
</head>
<body>

<section class="card card--front" aria-label="Business card front">
  <div class="brand-square"></div>
  <div class="brand-name">Bramblewood Coatings<br>Pty Ltd</div>

  <div class="contact-band">
    <div class="address">
      <strong>Bramblewood Coatings Pty Ltd.</strong><br>
      Larkspur St. No 18 Ferndale NSW<br>
      PO BOX 40718
    </div>
    <ul class="lines">
      <li>
        <svg viewBox="0 0 12 12"><path d="M2 1h3l1 3-1.5 1a6 6 0 0 0 2.5 2.5L8 6l3 1v3a1 1 0 0 1-1 1A9 9 0 0 1 1 2a1 1 0 0 1 1-1z" fill="var(--ink)"/></svg>
        (02) 6100 4827
      </li>
      <li>
        <svg viewBox="0 0 12 12"><rect x="3" y="0.5" width="6" height="11" rx="1" fill="none" stroke="var(--ink)"/><rect x="5" y="9" width="2" height="1" fill="var(--ink)"/></svg>
        0400 318 265
      </li>
      <li>
        <svg viewBox="0 0 12 12"><rect x="0.5" y="2.5" width="11" height="7" fill="none" stroke="var(--ink)"/><path d="M0.5 2.5 6 7l5.5-4.5" fill="none" stroke="var(--ink)"/></svg>
        dean@bramblewoodcoatings.com.au
      </li>
    </ul>
  </div>
</section>

<section class="card card--back" aria-label="Business card back">
  <div class="holder">
    <div class="holder-name">Dean Hartley</div>
    <div class="holder-role">founder</div>
  </div>

  <div class="brand-square"></div>
  <div class="brand-name">Bramblewood Coatings<br>Pty Ltd</div>

  <div class="services">
    <p>Interior/Exterior • Residential/Commercial • Special effects/Texture Coatings</p>
    <p>Water Damage Repair • Fully qualified • Pensioner Discount • 10 Year guarantee</p>
    <p>Fully Insured • Obligation free quotes</p>
  </div>
  <div class="website">www.bramblewoodcoatings.com.au</div>
</section>

</body>
</html>
```